Verpackungsdesign für Lifestyle-Diagnostik und Supplements im Bereich Longevity
Zielgruppe
Wir machen Lifestyle-Diagnostik und Supplements im Bereich Longevity
Aufgabenstellung
Verpackung eines Tests (wie der hier: https://shop.quellmora.com/products/zentrip) in der gezeigten Metallschachtel, Supplements in den gezeigten Dosen. Ein Set besteht aus einem Test und zwei Dosen (morgens und abends). Farbschema und Logo Korunelle wie im Anhang. paar Details zu den Supplements auch in den Dateien
Bitte auch an Prägung und anderen Gestaltungsmöglichkeiten denken

```html
<!DOCTYPE html>
<html lang="de">
<head>
<meta charset="utf-8">
<title>Korunelle – Etiketten Day- und Night-Complex</title>
<link rel="stylesheet" href="https://fonts.googleapis.com/css2?family=Montserrat:wght@400;600;700&display=swap">
<style>
  :root {
    --page-top: #f4f5f6;
    --page-bottom: #d9dcde;
    --teal-deep: #1d4850;
    --teal-mid: #0b6a73;
    --teal-bright: #08747c;
    --lime: #a6cd1e;
    --lime-bright: #b4d422;
    --olive: #6f9a2a;
    --white: #ffffff;
    --accent-text: #a9d12c;
  }
  * { margin: 0; padding: 0; box-sizing: border-box; }
  html, body { width: 1200px; height: 972px; overflow: hidden; }
  body {
    background: linear-gradient(180deg, var(--page-top), var(--page-bottom));
    font-family: "Montserrat", sans-serif;
    color: var(--white);
    position: relative;
  }
  .label {
    position: absolute;
    left: 160px;
    width: 880px;
    height: 440px;
    overflow: hidden;
  }
  .label--night {
    top: 36px;
    background:
      radial-gradient(ellipse 70% 55% at 55% 0%, rgba(8,116,124,0.85), rgba(8,116,124,0) 70%),
      linear-gradient(100deg, var(--teal-deep) 0%, var(--teal-deep) 38%, var(--olive) 68%, var(--lime) 88%, var(--lime-bright) 100%);
  }
  .label--day {
    top: 496px;
    background:
      radial-gradient(ellipse 75% 60% at 70% 100%, rgba(8,116,124,0.9), rgba(8,116,124,0) 70%),
      linear-gradient(100deg, var(--lime-bright) 0%, var(--lime) 14%, var(--olive) 36%, var(--teal-deep) 66%, var(--teal-deep) 100%);
  }
  .label__front {
    position: absolute;
    left: 0;
    width: 880px;
    top: 0;
    height: 440px;
    text-align: center;
  }
  .brand {
    position: absolute;
    top: 104px;
    left: 0;
    right: 0;
    font-size: 34px;
    font-weight: 700;
    letter-spacing: 0.5px;
    color: var(--white);
  }
  .brand__dot {
    display: block;
    width: 22px;
    height: 22px;
    border-radius: 50%;
    background: var(--white);
    margin: -48px auto 22px;
  }
  .product {
    position: absolute;
    top: 196px;
    left: 0;
    right: 0;
    font-size: 36px;
    font-weight: 700;
    color: var(--accent-text);
  }
  .icon {
    position: absolute;
    left: 405px;
    top: 268px;
    width: 70px;
    height: 70px;
  }
  .tagline {
    position: absolute;
    top: 376px;
    left: 0;
    right: 0;
    font-size: 22px;
    font-weight: 600;
  }
  .ingredients {
    position: absolute;
    right: 52px;
    bottom: 40px;
    writing-mode: vertical-rl;
    transform: rotate(180deg);
    font-size: 16px;
    line-height: 1.3;
  }
  .ingredients strong { font-weight: 700; }
</style>
</head>
<body>
  <section class="label label--night" aria-label="Etikett Night-Complex">
    <div class="label__front">
      <div class="brand"><span class="brand__dot"></span>Korunelle</div>
      <div class="product">Night-Complex</div>
      <svg class="icon" viewBox="0 0 70 70" aria-hidden="true">
        <path d="M30 8 A28 28 0 1 0 62 46 A24 24 0 0 1 30 8 Z" fill="none" stroke="var(--lime)" stroke-width="6" stroke-linejoin="round"/>
      </svg>
      <div class="tagline">Täglicher Baustein Zukunft</div>
    </div>
    <p class="ingredients">Hochreine Longevity-Wirkstoffe:<br><strong>NMN, Fisetin</strong></p>
  </section>

  <section class="label label--day" aria-label="Etikett Day-Complex">
    <div class="label__front">
      <div class="brand"><span class="brand__dot"></span>Korunelle</div>
      <div class="product">Day-Complex</div>
      <svg class="icon" viewBox="0 0 70 70" aria-hidden="true">
        <g stroke="var(--lime)" stroke-width="5" stroke-linecap="round" fill="none">
          <circle cx="35" cy="35" r="13"/>
          <line x1="35" y1="4" x2="35" y2="11"/>
          <line x1="35" y1="59" x2="35" y2="66"/>
          <line x1="4" y1="35" x2="11" y2="35"/>
          <line x1="59" y1="35" x2="66" y2="35"/>
          <line x1="13" y1="13" x2="18" y2="18"/>
          <line x1="52" y1="52" x2="57" y2="57"/>
          <line x1="13" y1="57" x2="18" y2="52"/>
          <line x1="52" y1="18" x2="57" y2="13"/>
        </g>
      </svg>
      <div class="tagline">Täglicher Baustein Zukunft</div>
    </div>
    <p class="ingredients">Hochreine Longevity-Wirkstoffe:<br><strong>NMN, Fisetin</strong></p>
  </section>
</body>
</html>
```